Web Design Project

Dear designer(s),

I need a design for a shop who's specialized into...

-Material to fix or do tailor made clothing (cloth, buttons, zippers etc)
-Curtains (static/pull-up)
-Blinds (plastic/wood)

that kind of stuff.

Good thing is that I can provide a lot of pretty photo's to work with. I have 3.5 Gigabyte of 300-1200 dpi photo's altho I converted most of them to 72dpi for your convenience (75Mb).

You can download the working material from this quellbin link:

http://files.quellbin.net/u/31920586/Velunor.zip

this is an updated file, it contains the dutch menu items to use in your design

http://files.quellbin.net/u/31920586/Velunor_Content.txt

Notice: take your time to come up with something nice. I prefer 1 or 2 designs from a designer that has been thinked of, than 5 quick ones.
Updates

Thank you for those who posted designs already but I want to clarify something.

As I mentioned it's a shop, that's a physical shop and not a webshop.

So you can safe some time and skip drawing the shopping cart icons, shop items on the homepage and other shop related things.

They don't want to start online reselling as they already spend most of their time in their shop to catch up with all orders.

Keep up the good work!

Industry/Entity Type

Clothing

Requirements
Nice to have
• Maybe the hi-res pictures can be used as background ratotor that appears left/right next to the centered website content?

Since there is a lot of material each section might have his topic linked set of thumbnails that opens a bigger image on clicking?

```html
<!DOCTYPE html>
<html lang="nl">
<head>
<meta charset="utf-8">
<title>Velunor – Stoffen, Tafellinnen, Raambekleding</title>
<link href="https://fonts.googleapis.com/css2?family=Questrial&display=swap" rel="stylesheet">
<style>
:root{
  --blue:#0a6bbd;
  --blue-dark:#0b4f96;
  --ink:#3a3a3a;
  --grey:#8a8a8a;
  --paper:#edeae3;
  --sky:#dde9f1;
  --rule:#b9b39f;
}
*{box-sizing:border-box;margin:0;padding:0}
html,body{width:925px;height:1200px;overflow:hidden;background:var(--paper)}
body{font-family:"Questrial",sans-serif;color:var(--ink);position:relative}
.page{position:relative;width:925px;height:1200px;overflow:hidden}

.masthead{position:absolute;left:0;top:0;width:925px;height:123px;background:var(--sky);border-bottom:3px solid #c9dbe6}
.brand{position:absolute;left:10px;top:48px;display:flex;align-items:center;gap:8px}
.brand-dot{width:16px;height:16px;border-radius:50%;background:var(--blue)}
.brand-name{font-size:42px;color:var(--blue);letter-spacing:-1px}
.tagline{position:absolute;left:250px;top:6px;font-size:16px;line-height:19px;color:var(--grey)}
.site-url{position:absolute;left:210px;top:78px;font-size:25px;color:var(--grey)}
.head-contact{position:absolute;right:8px;top:28px;text-align:right;color:var(--ink)}
.head-phone{font-size:27px;font-style:italic;display:flex;align-items:center;gap:8px;justify-content:flex-end}
.head-mail{font-size:16px;font-style:italic;margin-top:14px;display:flex;align-items:center;gap:10px;justify-content:flex-end}

.main-nav{position:absolute;top:142px;left:70px;display:flex;align-items:center}
.main-nav a{color:var(--blue);font-size:20px;text-decoration:none;margin-right:52px}
.main-nav a.current{background:var(--blue-dark);color:#fff;padding:12px 10px;border-top:3px solid var(--blue);margin-right:44px}

.hero{position:absolute;left:13px;top:210px;width:897px;height:356px;border-radius:26px;border:4px solid #e6eaee;
  background:linear-gradient(180deg,#b9c7d2 0%,#d8dde2 38%,#c7c8c5 62%,#8d8f8c 100%)}
.hero-caption{position:absolute;left:6px;top:120px;width:334px;height:88px;background:var(--blue-dark);color:#fff;padding:10px 14px}
.hero-caption h2{font-weight:400;font-size:34px;line-height:40px}
.hero-caption p{font-size:13px;margin-top:8px}

.thumbs{position:absolute;left:142px;top:566px;width:644px;height:78px;display:flex;padding:0 14px;
  background:#e2e2e0;border-radius:0 0 16px 16px}
.thumb{flex:1;border-right:1px solid #777}
.thumbs svg{position:absolute;top:22px}

.welcome{position:absolute;left:15px;top:686px;width:902px}
.welcome h1{font-weight:400;font-size:26px;color:var(--ink);padding-bottom:6px;border-bottom:1px solid var(--rule)}
.welcome h1 span{color:var(--blue);font-size:33px}
.welcome p{font-size:15.5px;line-height:21px;text-align:justify;margin-top:9px}
.welcome h3{font-weight:400;font-size:20px;color:var(--blue);margin-top:18px}
.welcome h3+p{margin-top:4px}
.read-more{position:absolute;right:-4px;top:212px;font-size:13px;font-style:italic;color:var(--blue-dark);background:#fff;padding:6px 12px;border-right:3px solid #ccc}

.contact-band{position:absolute;left:0;top:961px;width:925px;height:172px;background:var(--sky);border-top:3px solid #c9dbe6;border-bottom:3px solid #c9dbe6}
.contact-band h2{position:absolute;left:10px;top:14px;font-weight:400;font-size:28px;color:var(--ink)}
.contact-band .rule{position:absolute;left:120px;top:40px;width:342px;border-top:1px solid #888}
.contact-info{position:absolute;left:12px;top:58px;font-size:16px;font-style:italic;line-height:22px;color:#111}
.contact-lines{display:flex;gap:20px;margin-top:6px;color:var(--blue);font-size:18px}
.contact-lines span,.contact-mail{display:flex;align-items:center;gap:8px}
.contact-mail{color:var(--blue);font-size:18px;margin-top:6px}
.map{position:absolute;left:526px;top:18px;width:390px;height:140px;border:3px solid #fff;
  background:linear-gradient(135deg,#e9e4d4,#d9dfc8 60%,#e6e1d0)}

.footer{position:absolute;left:0;top:1140px;width:925px;text-align:center}
.footer small{font-size:10px;color:var(--ink)}
.footer .brand-name{display:block;font-size:20px;color:var(--grey);margin-top:2px}
</style>
</head>
<body>
<div class="page">
  <header class="masthead">
    <div class="tagline">Stoffen<br>Tafellinnen<br>Raambekleding</div>
    <div class="brand"><span class="brand-dot"></span><span class="brand-name">velunor</span></div>
    <div class="site-url">www.velunor.be</div>
    <div class="head-contact">
      <div class="head-phone">
        <svg width="22" height="26" viewBox="0 0 22 26"><path d="M4 2h4l2 6-3 2c1 4 4 7 8 8l2-3 5 2v5c-10 1-19-8-18-20z" fill="#0b4f96"/></svg>
        053.72.18.64</div>
      <div class="head-mail">
        <svg width="26" height="16" viewBox="0 0 26 16"><rect x="1" y="1" width="24" height="14" fill="none" stroke="#0a6bbd" stroke-width="2"/><path d="M1 1l12 8 12-8" fill="none" stroke="#0a6bbd" stroke-width="2"/></svg>
        velunor@brightmail.be</div>
    </div>
  </header>

  <nav class="main-nav">
    <a class="current" href="#">Home</a>
    <a href="#">Tafellinnen</a>
    <a href="#">Decoratiestoffen</a>
    <a href="#">Optreksystemen</a>
    <a href="#">Contact</a>
  </nav>

  <section class="hero" role="img" aria-label="Photo of a white linen cloth draped over driftwood on a pebble beach with glass bottles and a jug">
    <div class="hero-caption">
      <h2>Lorem ipsumdolor</h2>
      <p>Lorem ipsum dolor sit amet Loremips adipiscing elit.</p>
    </div>
  </section>

  <div class="thumbs">
    <div class="thumb" role="img" aria-label="Thumbnail: white cloth on beach" style="background:#c9cdd0"></div>
    <div class="thumb" role="img" aria-label="Thumbnail: striped fabrics" style="background:#a9a49a"></div>
    <div class="thumb" role="img" aria-label="Thumbnail: grey curtains" style="background:#6e7d8d"></div>
    <div class="thumb" role="img" aria-label="Thumbnail: dining room interior" style="background:#bdbab4"></div>
    <div class="thumb" role="img" aria-label="Thumbnail: red fabric" style="background:#b83a55"></div>
    <div class="thumb" role="img" aria-label="Thumbnail: kitchen with blinds" style="background:#7d8890"></div>
    <div class="thumb" role="img" aria-label="Thumbnail: shop front" style="background:#6c6558;border:none"></div>
    <svg style="left:2px" width="16" height="36" viewBox="0 0 16 36"><path d="M14 2L2 18l12 16" fill="none" stroke="#222" stroke-width="4"/></svg>
    <svg style="right:2px" width="16" height="36" viewBox="0 0 16 36"><path d="M2 2l12 16L2 34" fill="none" stroke="#1a8fd8" stroke-width="4"/></svg>
  </div>

  <main class="welcome">
    <h1>Welcom to <span>velunor</span></h1>
    <p>Velunor is al 40 jaar een gespecialiseerde zaak met een compleet product- en dienstenaanbod op he gebied van stoffen, mercerie, decoratie, raambekleding en tafellinnen.</p>
    <p>Wij garanderen u betrouwbare en constante kwaliteiten aan, persoonlijke opvolging op maat en advies.</p>
    <h3>Cloth - Fabric</h3>
    <p>Alle nieuwe collecties van dames-modestoffen, kinder-modestoffen, aangevuld met fornituren, accesoires, modebladen en patronen van de door ons gebruikte merken.</p>
    <a class="read-more">Read more...</a>
  </main>

  <section class="contact-band">
    <h2>Contact</h2>
    <div class="rule"></div>
    <div class="contact-info">
      Velunor<br>Kortestraat 14B, B-9230 Wettersen
      <div class="contact-lines">
        <span><svg width="22" height="16" viewBox="0 0 22 16"><path d="M1 6c6-6 14-6 20 0l-3 3-3-2V5H7v2L4 9z M5 10h12v5H5z" fill="#0a6bbd"/></svg>053.72.18.64</span>
        <span><svg width="22" height="18" viewBox="0 0 22 18"><rect x="5" y="1" width="12" height="6" fill="#0a6bbd"/><rect x="1" y="7" width="20" height="8" rx="2" fill="#0a6bbd"/></svg>053.72.19.27</span>
      </div>
      <div class="contact-mail"><svg width="22" height="14" viewBox="0 0 22 14"><rect x="1" y="1" width="20" height="12" fill="none" stroke="#0a6bbd" stroke-width="2"/><path d="M1 1l10 7 10-7" fill="none" stroke="#0a6bbd" stroke-width="2"/></svg>velunor@brightmail.be</div>
    </div>
    <div class="map" role="img" aria-label="Road map showing the shop location"></div>
  </section>

  <footer class="footer">
    <small>©Copyright 2013. All Rights Reserved</small>
    <span class="brand-name">velunor</span>
  </footer>
</div>
</body>
</html>
```